Business Cards and Stationery for a laboratory quality consulting business
Brennick Quality Solutions
Creative Brief
Simple
Marion Brennick
Principal Consultant
4817 Thistlewood Lane Cary, NC 27604
marion@brennickquality.example
www.brennickquality.example

```html
<!DOCTYPE html>
<html lang="en">
<head>
<meta charset="utf-8">
<title>Brennick Quality Solutions – Business Card</title>
<link href="https://fonts.googleapis.com/css2?family=Montserrat:wght@500;600;700&display=swap" rel="stylesheet">
<style>
  :root {
    --teal: #0f8282;
    --orange: #f9a11b;
    --white: #ffffff;
    --paper: #ffffff;
  }
  html, body {
    margin: 0;
    padding: 0;
    overflow: hidden;
    background: var(--paper);
  }
  .canvas {
    position: relative;
    width: 1200px;
    height: 1028px;
    overflow: hidden;
    background: var(--paper);
    font-family: "Montserrat", Arial, sans-serif;
  }
  .card {
    position: absolute;
    left: 314px;
    width: 600px;
    height: 337px;
  }
  .card--front { top: 93px; }
  .card--back { top: 560px; }
  .edge-band {
    position: absolute;
    left: 0;
    top: 0;
    width: 57px;
    height: 100%;
    background: var(--teal);
  }
  .brand-mark {
    position: absolute;
    left: 331px;
    top: 16px;
    display: flex;
    align-items: center;
    gap: 12px;
  }
  .brand-mark__dot {
    width: 34px;
    height: 34px;
    border-radius: 50%;
    background: var(--orange);
  }
  .brand-mark__name {
    font-size: 40px;
    font-weight: 700;
    color: var(--teal);
    letter-spacing: -0.5px;
  }
  .name-tag {
    position: absolute;
    left: 57px;
    top: 88px;
    width: 266px;
    height: 79px;
    background: var(--orange);
    color: var(--white);
    box-sizing: border-box;
    padding: 15px 0 0 11px;
    font-size: 22px;
    font-weight: 600;
    line-height: 1.3;
  }
  .contact {
    position: absolute;
    left: 68px;
    top: 196px;
    margin: 0;
    color: var(--teal);
    font-size: 22.5px;
    font-weight: 600;
    line-height: 1.38;
    font-style: normal;
  }
  .brand-tag {
    position: absolute;
    left: 57px;
    top: 80px;
    width: 274px;
    height: 80px;
    background: var(--orange);
    color: var(--white);
    box-sizing: border-box;
    padding: 0 14px;
    display: flex;
    align-items: center;
    font-size: 24px;
    font-weight: 700;
    line-height: 1.15;
  }
  .brand-tag__dot {
    position: absolute;
    left: 390px;
    top: 82px;
    width: 76px;
    height: 76px;
    border-radius: 50%;
    background: var(--teal);
  }
</style>
</head>
<body>
<main class="canvas">
  <section class="card card--front" aria-label="Business card front">
    <div class="edge-band"></div>
    <div class="brand-mark">
      <span class="brand-mark__dot"></span>
      <span class="brand-mark__name">Brennick</span>
    </div>
    <div class="name-tag">
      <div class="name-tag__name">Marion Brennick</div>
      <div class="name-tag__title">Principal Consultant</div>
    </div>
    <address class="contact">
      4817 Thistlewood Lane Cary, NC 27604<br>
      Cell: 919-555-0148<br>
      Email: marion@brennickquality.example<br>
      www.brennickquality.example
    </address>
  </section>

  <section class="card card--back" aria-label="Business card back">
    <div class="edge-band"></div>
    <div class="brand-tag">Brennick Quality Solutions</div>
    <span class="brand-tag__dot"></span>
  </section>
</main>
</body>
</html>
```